Morvela Aesthetic Doctor

I require an elegant, luxurious looking business card for my aesthetic business. I am a doctor and that will set me aside from competitors. I am planning to provide home and spa based treatments to clients with high expectations. I have attached my logo.

```html
<!DOCTYPE html>
<html lang="en">
<head>
<meta charset="utf-8">
<title>Morvela Aesthetic Doctor – Business Card</title>
<link href="https://fonts.googleapis.com/css2?family=Montserrat:wght@400;500;600&display=swap" rel="stylesheet">
<style>
  :root {
    --backdrop: #1c1c1f;
    --card-white: #ffffff;
    --card-charcoal: #3e3e41;
    --brand-blue: #1ea0e6;
    --text-grey: #4a4a4d;
    --text-light: #f2f2f2;
    --ring-grey: #9a9a9e;
  }
  * { box-sizing: border-box; margin: 0; padding: 0; }
  html, body { width: 1200px; height: 786px; overflow: hidden; }
  body {
    background: var(--backdrop);
    font-family: "Montserrat", sans-serif;
    position: relative;
  }
  .card {
    position: absolute;
    width: 540px;
    height: 309px;
    overflow: hidden;
    box-shadow: 0 18px 40px rgba(0,0,0,0.45);
  }
  .card-front { left: 40px; top: 238px; background: var(--card-white); }
  .card-back { left: 620px; top: 238px; background: var(--card-charcoal); }
  .front-waves { position: absolute; inset: 0; }

  .doctor-block {
    position: absolute;
    right: 28px;
    top: 18px;
    text-align: right;
  }
  .doctor-name {
    color: var(--brand-blue);
    font-weight: 600;
    font-size: 16px;
    letter-spacing: 0.2px;
  }
  .doctor-credential {
    color: var(--text-grey);
    font-size: 11px;
    line-height: 1.35;
    margin-top: 3px;
  }

  .brand-lockup {
    position: absolute;
    display: flex;
    align-items: center;
    gap: 12px;
  }
  .card-front .brand-lockup { left: 34px; top: 126px; }
  .brand-ring {
    border: 2px solid var(--ring-grey);
    border-radius: 50%;
    flex: none;
  }
  .card-front .brand-ring { width: 50px; height: 50px; }
  .brand-name {
    color: var(--brand-blue);
    font-weight: 500;
    line-height: 1.15;
    letter-spacing: 1.5px;
    text-transform: uppercase;
  }
  .card-front .brand-name { font-size: 15px; }

  .contact-list {
    position: absolute;
    right: 24px;
    top: 176px;
    list-style: none;
    text-align: right;
    color: var(--text-light);
    font-size: 11px;
    line-height: 1.7;
  }
  .contact-list li { display: flex; align-items: center; justify-content: flex-end; gap: 6px; }
  .contact-icon { width: 10px; height: 10px; flex: none; }

  .card-back .brand-lockup {
    left: 50%;
    top: 66px;
    transform: translateX(-50%);
    gap: 16px;
  }
  .card-back .brand-ring { width: 74px; height: 74px; }
  .card-back .brand-name { font-size: 22px; white-space: nowrap; }

  .service-list {
    position: absolute;
    left: 0;
    right: 0;
    top: 176px;
    text-align: center;
    color: var(--text-light);
    font-size: 13px;
    line-height: 1.75;
    letter-spacing: 0.4px;
  }
  .divider { color: var(--brand-blue); margin: 0 4px; }
  .service-tagline { text-transform: uppercase; letter-spacing: 1px; }
</style>
</head>
<body>

<section class="card card-front">
  <svg class="front-waves" viewBox="0 0 540 309" width="540" height="309" aria-hidden="true">
    <path d="M540 100 C425 100 388 145 358 198 C322 262 250 302 120 309 L540 309 Z" fill="var(--card-charcoal)"/>
    <path d="M540 87 C412 87 372 132 342 188 C306 252 236 298 100 309" fill="none" stroke="var(--card-charcoal)" stroke-width="5"/>
    <path d="M326 132 C298 222 215 282 -4 292" fill="none" stroke="var(--brand-blue)" stroke-width="7" stroke-linecap="round"/>
  </svg>

  <div class="doctor-block">
    <p class="doctor-name">Dr Elise Varnow MRCPCH MD</p>
    <p class="doctor-credential">Australasian Diploma<br>of Aesthetic Medicine</p>
  </div>

  <div class="brand-lockup">
    <span class="brand-ring"></span>
    <p class="brand-name">Morvela<br>Aesthetic Doctor</p>
  </div>

  <ul class="contact-list">
    <li>0800 555 014
      <svg class="contact-icon" viewBox="0 0 10 10"><path d="M2 1 L4 1 L4.6 3 L3.4 3.8 C4 5.2 4.8 6 6.2 6.6 L7 5.4 L9 6 L9 8 C5 8.4 1.6 5 2 1 Z" fill="var(--brand-blue)"/></svg>
    </li>
    <li>elise@morvela.co.nz
      <svg class="contact-icon" viewBox="0 0 10 10"><rect x="1" y="2.5" width="8" height="5.5" fill="none" stroke="var(--brand-blue)" stroke-width="1"/><path d="M1 2.5 L5 5.5 L9 2.5" fill="none" stroke="var(--brand-blue)" stroke-width="1"/></svg>
    </li>
    <li>www.morvela.co.nz
      <svg class="contact-icon" viewBox="0 0 10 10"><circle cx="5" cy="5" r="4" fill="none" stroke="var(--brand-blue)" stroke-width="1"/><path d="M1 5 H9 M5 1 C3 3 3 7 5 9 M5 1 C7 3 7 7 5 9" fill="none" stroke="var(--brand-blue)" stroke-width="0.8"/></svg>
    </li>
  </ul>
</section>

<section class="card card-back">
  <div class="brand-lockup">
    <span class="brand-ring"></span>
    <p class="brand-name">Morvela<br>Aesthetic Doctor</p>
  </div>

  <div class="service-list">
    <p>Dermal injectables<span class="divider">|</span>Plasma facials<span class="divider">|</span>Microneedling</p>
    <p>Skin boosters<span class="divider">|</span>Excessive sweating</p>
    <p class="service-tagline">Home and spa based treatments</p>
  </div>
</section>

</body>
</html>
```